Author Felicia Moten Cover Design for "Velvet Ledger"

I want a design that reflects the following synopsis. However, my brand colors are orange, black, and white. I like the theme of my original cover that's attached, but I also like how the other attached book cover really attracts the eye with the way the green pops out.

"Velvet Ledger" synopsis is as follows: What's the first sign that lets you know you're dealing with a sociopath? Velvet Ledger is riddled with the clues. Set in the new reigning hub of African-American drama - suburban Atlanta - it's the scandalous saga of the ambitious and untamed Dwayne Holloway that chronicles his descent into the dismal world of irrationality. From high school to college and throughout the pros - his story will have you watching your back ever so closely. Dwayne had two dreams - to play in the UGL and to make the cover of Arena Weekly. When the former was cut short by a serious injury, all the fame, fortune, parties, and women were gone. On the contrary, his best friend since childhood, Terrence Bly, was on top of the world - a successful business, a beautiful wife, a fat bank account... he seemed to have it all. Being a supportive friend, Terrence offers Dwayne a job, hoping that Dwayne would have a positive impact on his company. But when jealousy and murder come between them, which one will fall? Could Dwayne be so callous that he'd set up his best friend? Is Terrence capable of unleashing his own wrath? They solved the riddle. Can you?

```html
<!DOCTYPE html>
<html lang="en">
<head>
<meta charset="utf-8">
<title>Velvet Ledger — Felicia Moten</title>
<link href="https://fonts.googleapis.com/css2?family=Carlito:wght@400;700&display=swap" rel="stylesheet">
<style>
  :root {
    --ink: #000000;
    --glow: #1f5a12;
    --glow-deep: #0c2608;
    --swirl: #5fe03a;
    --swirl-dark: #1c4a12;
    --text: #ececec;
    --title: #d9d9d9;
  }
  html, body {
    margin: 0;
    padding: 0;
    width: 1200px;
    height: 1000px;
    overflow: hidden;
    background: var(--ink);
  }
  .cover {
    position: relative;
    width: 1200px;
    height: 1000px;
    overflow: hidden;
    font-family: "Carlito", "Calibri", sans-serif;
    background:
      radial-gradient(ellipse 420px 520px at 270px 470px, var(--glow) 0%, var(--glow-deep) 45%, rgba(0,0,0,0) 80%),
      radial-gradient(ellipse 330px 460px at 1130px 450px, var(--glow-deep) 0%, rgba(0,0,0,0) 75%),
      var(--ink);
  }
  .back-blurb {
    position: absolute;
    left: 42px;
    top: 158px;
    width: 490px;
    margin: 0;
    color: var(--text);
    font-size: 19.4px;
    line-height: 29.1px;
    text-align: justify;
    hyphens: auto;
    -webkit-hyphens: auto;
  }
  .spine-text {
    position: absolute;
    writing-mode: vertical-rl;
    color: var(--title);
    font-size: 45px;
    line-height: 1;
    left: 574px;
    white-space: nowrap;
  }
  .spine-title { top: 142px; }
  .spine-author { top: 628px; }
  .front-title {
    position: absolute;
    left: 664px;
    top: 72px;
    margin: 0;
    font-weight: 400;
    font-size: 62px;
    line-height: 1;
    color: var(--title);
    white-space: nowrap;
  }
  .front-art {
    position: absolute;
    left: 660px;
    top: 225px;
    width: 490px;
    height: 420px;
  }
  .front-author {
    position: absolute;
    left: 748px;
    top: 862px;
    margin: 0;
    font-size: 50px;
    line-height: 1;
    color: var(--title);
    white-space: nowrap;
  }
</style>
</head>
<body>
<div class="cover">
  <p class="back-blurb">What's the first sign that lets you know you're dealing with a sociopath? Velvet Ledger is riddled with the clues. Set in the new reigning hub of African-American drama - suburban Atlanta - it's the scandalous saga of the ambitious and untamed Dwayne Holloway that chronicles his descent into the dismal world of irrationality. From high school to college and throughout the pros - his story will have you watching your back ever so closely. Dwayne had two dreams - to play in the UGL and to make the cover of Arena Weekly. When the former was cut short by a serious injury, all the fame, fortune, parties, and women were gone. On the contrary, his best friend since childhood, Terrence Bly, was on top of the world - a successful business, a beautiful wife, a fat bank account... he seemed to have it all. Being a supportive friend, Terrence offers Dwayne a job, hoping that Dwayne would have a positive impact on his company. But when jealousy and murder come between them, which one will fall? Could Dwayne be so callous that he'd set up his best friend? Is Terrence capable of unleashing his own wrath? They solved the riddle. Can you?</p>

  <div class="spine-text spine-title">Velvet Ledger</div>
  <div class="spine-text spine-author">Felicia Moten</div>

  <h1 class="front-title">Velvet Ledger</h1>

  <svg class="front-art" viewBox="0 0 490 420" role="img" aria-label="Glowing green swirl vortex with a portrait of a man in a suit at its centre">
    <defs>
      <radialGradient id="swirlGlow" cx="50%" cy="50%" r="50%">
        <stop offset="0%" stop-color="#6b5a3a"/>
        <stop offset="22%" stop-color="#2f6a1e"/>
        <stop offset="50%" stop-color="#5fe03a" stop-opacity="0.75"/>
        <stop offset="75%" stop-color="#1c4a12" stop-opacity="0.5"/>
        <stop offset="100%" stop-color="#000000" stop-opacity="0"/>
      </radialGradient>
    </defs>
    <ellipse cx="245" cy="215" rx="245" ry="205" fill="url(#swirlGlow)"/>
  </svg>

  <p class="front-author">Felicia Moten</p>
</div>
</body>
</html>
```